PuraVeln

Hi, We are looking for a design Label for our Packaged Drinking Water. We want a label in rich color. The current Label is uploaded. We wish for a much brighter color rather than black. Our current label is in black. We have attached other company labels to give you idea. The Solmira bottle image is also uploaded they use sticker for their bottle, front sticker contains name and back sticker's inner portion has graphics and the outer side has information we also open to that.
Industry/Entity Type
Packaged Drinking Water Bottle Brand
Look and feel
Each slider illustrates characteristics of the customer's brand and the style your logo design should communicate.

```html
<!DOCTYPE html>
<html lang="en">
<head>
<meta charset="utf-8">
<title>PuraVeln – Packaged Drinking Water Label</title>
<link rel="stylesheet" href="https://fonts.googleapis.com/css2?family=Poppins:wght@500;700&display=swap">
<style>
  :root {
    --page-bg: #f1f1f1;
    --label-blue: #1aa8d6;
    --label-blue-light: #52c4ea;
    --label-blue-deep: #1496c6;
    --ink-white: #ffffff;
  }
  html, body {
    margin: 0;
    padding: 0;
    width: 800px;
    height: 1200px;
    overflow: hidden;
    background: var(--page-bg);
  }
  .canvas {
    position: relative;
    width: 800px;
    height: 1200px;
  }
  .label {
    position: absolute;
    left: 40px;
    top: 205px;
    width: 720px;
    height: 790px;
    overflow: hidden;
    background: var(--label-blue);
  }
  .label-artwork {
    position: absolute;
    inset: 0;
    background:
      radial-gradient(ellipse 60% 45% at 25% 80%, var(--label-blue-light) 0%, transparent 70%),
      radial-gradient(ellipse 55% 40% at 85% 20%, var(--label-blue-light) 0%, transparent 70%),
      linear-gradient(160deg, var(--label-blue) 0%, var(--label-blue-deep) 100%);
  }
  .brand-name {
    position: absolute;
    left: 0;
    right: 0;
    top: 265px;
    margin: 0;
    text-align: center;
    font-family: "Poppins", sans-serif;
    font-weight: 700;
    font-size: 124px;
    line-height: 1;
    letter-spacing: -2px;
    color: var(--ink-white);
  }
  .product-type {
    position: absolute;
    left: 0;
    right: 0;
    top: 420px;
    margin: 0;
    text-align: center;
    font-family: "Poppins", sans-serif;
    font-weight: 500;
    font-size: 35px;
    letter-spacing: 1px;
    color: var(--ink-white);
  }
  .volume-badge {
    position: absolute;
    left: 308px;
    top: 575px;
    width: 90px;
    height: 120px;
  }
</style>
</head>
<body>
  <main class="canvas">
    <section class="label">
      <div class="label-artwork" role="img" aria-label="Fine-line leaf illustration in light and deep blue tones"></div>
      <h1 class="brand-name">PuraVeln</h1>
      <p class="product-type">PACKAGED DRINKING WATER</p>
      <svg class="volume-badge" viewBox="0 0 90 120" aria-label="1 litre">
        <path d="M45 4 C45 4 8 52 8 78 A37 37 0 0 0 82 78 C82 52 45 4 45 4 Z" fill="var(--ink-white)"/>
        <text x="45" y="94" text-anchor="middle" font-family="Poppins, sans-serif" font-weight="700" font-size="30" fill="var(--label-blue)">1L</text>
      </svg>
    </section>
  </main>
</body>
</html>
```